Flyer Template Design

I have attached 4 files. I would like a design template that could be used across these documents so that they have a common look and feel. The content of the documents is tested and should not be changed significantly. The images can be changed. I have also attache our logo for color compatibility.
Updates

Need extra days to review

Target Market(s)

Wealthy Christian donors

Font styles to use
Serif
Sans Serif

```html
<!DOCTYPE html>
<html lang="en">
<head>
<meta charset="utf-8">
<title>The Final Lap</title>
<link rel="stylesheet" href="https://fonts.googleapis.com/css2?family=Poppins:wght@300;400&family=Source+Sans+3:wght@400;600&display=swap">
<style>
  :root{
    --sky-blue:#00b4ec;
    --deep-blue:#0099dd;
    --ink:#2b2b2b;
    --page:#ffffff;
    --backdrop:#e4e4e4;
    --cloud-bottom:#a9dbf5;
    --brand-green:#1aa64a;
  }
  *{margin:0;padding:0;box-sizing:border-box}
  html,body{width:1108px;height:1200px;overflow:hidden;background:var(--backdrop)}
  .flyer{
    position:absolute;left:117px;top:0;width:873px;height:1200px;
    background:linear-gradient(180deg,var(--page) 0,var(--page) 760px,#eaf6fd 880px,var(--cloud-bottom) 1130px);
    font-family:"Source Sans 3","Myriad Pro",sans-serif;color:var(--ink);overflow:hidden;
  }
  .spine-shade{position:absolute;top:100px;left:0;width:873px;height:460px;
    background:linear-gradient(90deg,rgba(0,0,0,0) 0,rgba(0,0,0,0) 340px,rgba(0,0,0,.05) 436px,rgba(0,0,0,0) 470px)}
  .frame-svg{position:absolute;left:0;top:0}
  .title{position:absolute;top:28px;left:0;width:100%;text-align:center;
    font-family:"Poppins",sans-serif;font-weight:300;font-size:45px;color:#fff;letter-spacing:.3px}
  .column{position:absolute;text-align:center}
  .column p{margin-bottom:12px}
  .col-left{left:53px;width:332px;top:134px;font-size:17.5px;line-height:19.7px}
  .col-right{left:462px;width:386px;top:132px}
  .section-head{font-family:"Source Sans 3",sans-serif;font-weight:400;font-size:25px;line-height:30px;margin:4px 0 12px;letter-spacing:.2px}
  .lead{font-size:20.5px;line-height:26px;margin-bottom:10px;padding:0 28px}
  .col-right .body{font-size:16px;line-height:18.2px;margin-bottom:10px}
  .closer{font-size:25.5px;line-height:30px;margin-top:2px}
  .people-strip{position:absolute;left:0;top:559px;width:873px;height:150px;
    background:linear-gradient(90deg,#4a2a1f,#c2363a 15%,#8a5a3a 30%,#2a7fc4 40%,#d9a23a 52%,#c9c3b5 62%,#2b2526 72%,#e1d7c0 82%,#c7891e)}
  .sprint{position:absolute;top:728px;left:126px;width:621px;text-align:center}
  .sprint-head{font-family:"Poppins",sans-serif;font-weight:400;font-size:28px;letter-spacing:.6px;margin-bottom:10px}
  .sprint p{font-size:14.5px;line-height:18px}
  .sprint .callout{font-size:19px;font-weight:600;margin:14px 0 18px}
  .sprint .bold{font-weight:600;margin-top:15px}
  .brand{position:absolute;top:1052px;left:0;width:873px;display:flex;justify-content:center;align-items:center;gap:18px}
  .brand-mark{width:56px;height:56px;background:var(--brand-green)}
  .brand-name{font-family:"Source Sans 3",sans-serif;font-weight:600;font-size:22px;line-height:24px;color:var(--ink);letter-spacing:.5px}
</style>
</head>
<body>
<main class="flyer">
  <div class="spine-shade"></div>
  <svg class="frame-svg" width="873" height="1200" viewBox="0 0 873 1200" aria-hidden="true">
    <defs>
      <linearGradient id="bandGrad" x1="0" y1="0" x2="0" y2="1">
        <stop offset="0" stop-color="#00c2ef"/>
        <stop offset="1" stop-color="#0aa4e3"/>
      </linearGradient>
    </defs>
    <path d="M0,0 H873 V104 Q560,96 436,150 Q313,96 0,104 Z" fill="url(#bandGrad)"/>
    <path d="M0,1126 Q320,1120 436,1165 Q553,1120 873,1126 V1200 H0 Z" fill="url(#bandGrad)"/>
  </svg>

  <h1 class="title">The Final Lap</h1>

  <section class="column col-left">
    <p>Every four years, the Summit Games Marathon is run through the streets of the host city. The final lap, though, is always run in the Games Stadium. At the end of the race, the runners burst into the stadium for the final lap, and the crowd explodes in celebration of a long race well run.</p>
    <p>For 2000 years, the church has been running a Marathon, racing to fulfill the Lord's command to “make disciples of all nations.” But now we're nearly done: we've come into the stadium; we're on the final lap. And the heavenly crowd is standing and cheering!</p>
    <h2 class="section-head">THE FINISH LINE</h2>
    <p>The Lord himself defined the finish line when he said, “This gospel of the kingdom will be preached in the whole world as a testimony to all nations, and then the end will come.”</p>
  </section>

  <section class="column col-right">
    <h2 class="section-head">WHEN WILL THE RACE END?</h2>
    <p class="lead">The Lord said, when the gospel has been proclaimed to “all nations.”</p>
    <p class="body">In the Bible, the word “nations” refers to people groups: groups of people who share a common ethnicity, culture, and language. Amazingly, there are about 12,000 of these “nations” around the world—and the Lord commanded us to make disciples in all of them!</p>
    <p class="body">Today, there are still about 500 people groups around the world have never heard the gospel. Most of these remaining groups are small and located in remote, difficult places. But now that we know who and where they are, by God's grace it is possible for us to engage every one of them with the gospel within the next 3 years.</p>
    <p class="closer">In other words, after a long race, we're on the final lap!</p>
  </section>

  <div class="people-strip" role="img" aria-label="Row of portrait photographs of people from many cultures and people groups around the world"></div>

  <section class="sprint">
    <h2 class="sprint-head">SPRINTING TO THE FINISH</h2>
    <p>In his second letter, an early apostle instructs believers “to hasten the coming of the day of God.” As the end of the race draws near, he's saying, we should sprint toward the finish line, striving to finish the race as quickly as we can.</p>
    <p class="callout">You can be part of the sprint to the finish.</p>
    <p>Partner with the Harvest Relay Fund and finance the missionaries who are taking the gospel for the first time to those last remaining people groups. Your investment will “hasten the coming of the day of God” by accelerating the effort to “make disciples of every nation.” In 2018, our partners sent the gospel to 231 people groups in 35 countries.</p>
    <p class="bold">Join us as we invest to make disciples in “all nations” by 2022.</p>
    <p class="bold">To learn more, email Dan Mercer at dmercer@harvestrelay.org.</p>
  </section>

  <div class="brand">
    <span class="brand-mark"></span>
    <span class="brand-name">THE<br>HARVEST RELAY<br>FUND</span>
  </div>
</main>
</body>
</html>
```